Business Card: RW Office Partners - Your tidy answer finder

Business Name: RW Office Partners
Website: www.rwofficepartners.com.au
Email: marisol@rwofficepartners.com.au
Mobile: 61 487 902 346
Facebook: @rwofficepartners
Instrgram: @rwofficepartners

Brading Colours:
HEX
#986474
#ddccd3
#7a8498
#c9d8e4
#000000
#ffffff

Tag Line: Your organised problem solver

Link to DRAFT website:
https://helpdeskhub.sitebuilderx.com/rw-office-partners

About Page from the website:
My name is Marisol Bramwell, and I would love to assist you to become more productive in your day to day and achieve your business and personal goals.
My mission is to give you time, time to work on the important tasks of your business or to be able to spend more time with your family. I will take on the tasks you don’t have time for, don’t know well or simply don’t like to do.
I have an extensive background in Administration, Tender Coordination, Document Control, WHS and Quality Management working primarily in the Construction, Mining and Corporate World.
I am passionate about being organised, having order and making things in your life (and mine) easier! I love to watch something unfold and grow into something amazing! I am known for being the go-to problem solver, the organiser of all things, producing high standards of work even under pressure. I’m also a confident communicator, and I understand that you’re busy running your business.

Target Market(s)

Small to Medium Business who require assistance in their business by a virtual assistant.

Industry/Entity Type

Virtual Assistant

Contact Information for Business Card

Mobile: 61 487 902 346

Font styles to use
Sans Serif

Colors
ffffff

Requirements
Must have
• Branding Colours as outlined.
Contact Details as outlined.
Logo as provided.
Proper contact details - mobile, facebook, instragm, website.
Simple, Elegant, very clean looking.
Should not have
• Note cute with pictures.
Not too girly as still want to market to construction companies.

```html
<!DOCTYPE html>
<html lang="en">
<head>
<meta charset="utf-8">
<title>RW Office Partners – Business Card</title>
<link rel="stylesheet" href="https://fonts.googleapis.com/css2?family=Montserrat:wght@500;600;700&family=Open+Sans:wght@400&display=swap">
<style>
  :root {
    --mauve: #986474;
    --mauve-light: #ddccd3;
    --slate: #7a8498;
    --mist: #c9d8e4;
    --ink: #3a3a3f;
    --white: #ffffff;
    --backdrop: #e9e9ec;
  }
  * { box-sizing: border-box; margin: 0; padding: 0; }
  html, body {
    width: 1200px; height: 1000px; overflow: hidden;
    background: var(--backdrop);
  }
  .sheet { position: relative; width: 1200px; height: 1000px; }
  .card {
    position: absolute; left: 220px; width: 760px; height: 434px;
    border-radius: 26px; overflow: hidden;
    box-shadow: 0 10px 30px rgba(0,0,0,0.12);
  }
  .card--front { top: 40px; background: var(--mauve); }
  .card--back  { top: 516px; background: var(--white); }

  /* Front */
  .front-brand {
    position: absolute; left: 0; right: 0; top: 150px;
    display: flex; align-items: center; justify-content: center; gap: 18px;
  }
  .brand-mark { width: 22px; height: 22px; background: var(--white); }
  .front-brand .brand-name {
    font-family: "Montserrat", sans-serif; font-weight: 600;
    font-size: 52px; letter-spacing: 1px; color: var(--white);
    text-transform: uppercase; line-height: 1;
  }
  .front-tagline {
    position: absolute; left: 0; right: 0; bottom: 62px;
    display: flex; align-items: center; gap: 22px;
  }
  .front-tagline .rule { flex: 1; height: 1.5px; background: var(--white); }
  .front-tagline p {
    font-family: "Open Sans", sans-serif; font-size: 17px;
    color: var(--white); letter-spacing: 0.5px; white-space: nowrap;
  }

  /* Back */
  .back-brand {
    position: absolute; left: 60px; top: 60px;
    display: flex; align-items: center; gap: 14px;
  }
  .back-brand .brand-mark { width: 16px; height: 16px; background: var(--mauve); }
  .back-brand .brand-name {
    font-family: "Montserrat", sans-serif; font-weight: 600;
    font-size: 30px; letter-spacing: 1px; color: var(--mauve);
    text-transform: uppercase; line-height: 1;
  }
  .back-rule {
    position: absolute; left: 40px; top: 200px; width: 560px;
    height: 1.5px; background: var(--slate);
  }
  .contact-list {
    position: absolute; left: 46px; top: 232px; list-style: none;
    font-family: "Open Sans", sans-serif; font-size: 19px; color: var(--ink);
  }
  .contact-list li {
    display: flex; align-items: center; gap: 12px; height: 31px;
  }
  .contact-list svg { width: 15px; height: 15px; flex: none; }
  .contact-list .icon-square {
    width: 13px; height: 13px; background: var(--mauve); border-radius: 2px; flex: none; margin: 0 1px;
  }
  .person {
    position: absolute; right: 60px; top: 322px; text-align: right;
  }
  .person-name {
    font-family: "Montserrat", sans-serif; font-weight: 700;
    font-size: 34px; color: var(--mauve); letter-spacing: 1px; line-height: 1.2;
  }
  .person-role {
    font-family: "Montserrat", sans-serif; font-weight: 500;
    font-size: 20px; color: var(--slate); letter-spacing: 1px; margin-top: 4px;
  }
  .edge-tab {
    position: absolute; right: 0; top: 330px; width: 14px; height: 64px;
    background: var(--mauve); border-radius: 8px 0 0 8px;
  }
</style>
</head>
<body>
<main class="sheet">

  <section class="card card--front" aria-label="Card front">
    <div class="front-brand">
      <span class="brand-mark"></span>
      <span class="brand-name">RW Office Partners</span>
    </div>
    <div class="front-tagline">
      <span class="rule"></span>
      <p>Your tidy answer finder</p>
      <span class="rule"></span>
    </div>
  </section>

  <section class="card card--back" aria-label="Card back">
    <div class="back-brand">
      <span class="brand-mark"></span>
      <span class="brand-name">RW Office Partners</span>
    </div>
    <div class="back-rule"></div>

    <ul class="contact-list">
      <li>
        <svg viewBox="0 0 24 24" fill="var(--mauve)" aria-hidden="true"><path d="M6.6 10.8a15.1 15.1 0 0 0 6.6 6.6l2.2-2.2a1 1 0 0 1 1-.25 11.4 11.4 0 0 0 3.6.57 1 1 0 0 1 1 1V20a1 1 0 0 1-1 1A17 17 0 0 1 3 4a1 1 0 0 1 1-1h3.5a1 1 0 0 1 1 1c0 1.25.2 2.45.57 3.57a1 1 0 0 1-.25 1z"/></svg>
        61 487 902 346
      </li>
      <li>
        <svg viewBox="0 0 24 24" fill="var(--mauve)" aria-hidden="true"><path d="M2 5h20v14H2z"/><path d="M2 5l10 8 10-8" fill="none" stroke="var(--white)" stroke-width="1.8"/></svg>
        marisol@rwofficepartners.com.au
      </li>
      <li>
        <svg viewBox="0 0 24 24" aria-hidden="true"><circle cx="12" cy="12" r="10" fill="var(--mauve)"/><path d="M2 12h20M12 2c3 3 3 17 0 20M12 2c-3 3-3 17 0 20" fill="none" stroke="var(--white)" stroke-width="1.4"/></svg>
        www.rwofficepartners.com.au
      </li>
      <li><span class="icon-square"></span>@rwofficepartners</li>
      <li><span class="icon-square"></span>@rwofficepartners</li>
    </ul>

    <div class="person">
      <div class="person-name">Daniel R. Ashford</div>
      <div class="person-role">Project Manager</div>
    </div>
    <div class="edge-tab"></div>
  </section>

</main>
</body>
</html>
```